Yoga Workshop - Yoga Practice information flyer

I am a yoga teacher who will be presenting a workshop on yoga for sleep and need a brochure for my clients which outlines a practice that I give them so they can do the practice at home. Ideally I would like a brochure that is a single A3 size of paper in size that folds in half to an A4 booklet with the entire practice on the centre section to make it easy for people to do the practice at home with just one open page in front of them:
* Front page detailing "Yoga for Sleep Workshop" and "Restorative Yoga Practice"
* Centre contains the information on the practice contained in the attached word document. The practice consists of 5 postures, so there needs to be five separate sections which have the pictures of the postures (attached in uploaded files) and the wording contained in the attached word document. All pictures uploaded need to be included in the flyer as each posture has different pictures demonstrating the posture using yoga props or using things people have at home
* Back page containing a picture of myself (picture uploaded in files) with some information about me (contained in the attached word document) and my website www.lunavesperflow.com.au

I also need this flyer to be able to printed on 2 double sided A4 sheets of paper so will require 2 x pdf file versions. Importantly, for the centre section of the flyer, the design needs to ensure if it is printed on A4 paper, the wording and pictures for each of the postures are not separated over two pages

Target Market(s)

Existing clients

Requirements
Must have
• Detailed in project description
Nice to have
• The word document also contains some quotes. These do not need to be included in the flyer. If there is room and there is room for one or two of those please include where it would look good
Should not have
• Stock pictures of people in yoga postures which a normal everyday person could not get into

```html
<!DOCTYPE html>
<html lang="en">
<head>
<meta charset="utf-8">
<title>Yoga for Sleep Workshop – Restorative Yoga Practice</title>
<link href="https://fonts.googleapis.com/css2?family=Alegreya:wght@700&family=Bebas+Neue&family=Barlow+Semi+Condensed:wght@600;700&family=Source+Sans+3:wght@400;600&display=swap" rel="stylesheet">
<style>
:root{
  --backdrop:#8a8a8a;
  --navy:#2e4460;
  --navy-ink:#2f4463;
  --copper:#c47b57;
  --peach:#fde0d6;
  --paper:#ffffff;
  --body-ink:#3a3a3a;
  --on-navy:#ffffff;
}
*{box-sizing:border-box;margin:0;padding:0}
html,body{width:814px;height:1200px;overflow:hidden}
body{background:var(--backdrop);position:relative;font-family:"Source Sans 3",Arial,sans-serif;color:var(--body-ink)}
.page{position:absolute;width:365px;height:517px;background:var(--paper);overflow:hidden}
.page--cover{left:28px;top:53px}
.page--sequence-a{left:421px;top:53px}
.page--sequence-b{left:28px;top:608px}
.page--about{left:421px;top:608px;background:var(--navy)}
.abs{position:absolute}

/* cover */
.cover-photo{left:60px;top:109px;width:305px;height:320px;background:linear-gradient(160deg,#3f5a2c 0%,#6f7d45 35%,#8aa0b8 60%,#2a2a2a 85%,#d9cfc4 100%)}
.cover-band{left:0;top:429px;width:365px;height:88px;background:var(--navy)}
.cover-curve{left:0;top:0}
.brand{left:100px;top:20px;width:265px;text-align:center}
.brand-dot{width:26px;height:26px;border:2px solid var(--copper);border-radius:50%;margin:0 auto 5px}
.brand-name{font-family:"Alegreya",Georgia,serif;font-weight:700;font-size:20px;color:var(--navy-ink);line-height:1}
.brand-tagline{font-size:6.8px;letter-spacing:1.3px;color:var(--navy-ink);margin-top:8px}
.cover-title{right:22px;top:443px;text-align:right;font-family:"Bebas Neue",Impact,sans-serif;font-size:22.5px;line-height:23px;color:var(--on-navy);letter-spacing:.2px}

/* sequence */
.sequence-title{left:23px;top:16px;font-family:"Barlow Semi Condensed",Arial,sans-serif;font-weight:600;font-size:12.6px;color:var(--navy-ink)}
.sequence-intro{left:23px;top:41px;width:319px;font-size:5.6px;line-height:7.4px}
.sequence-intro p+p{margin-top:7px}
.card{position:absolute;left:23px;width:319px;background:var(--peach);border-radius:5px}
.tag{position:absolute;background:var(--copper);color:#fff;font-family:"Barlow Semi Condensed",Arial,sans-serif;font-weight:700;font-size:9px;line-height:13px;height:13px;padding:0 7px 0 6px;border-radius:0 7px 7px 0}
.posture-name{position:absolute;font-family:"Barlow Semi Condensed",Arial,sans-serif;font-weight:600;font-size:8.6px;line-height:10.3px;color:var(--navy-ink)}
.note{position:absolute;font-size:4.9px;line-height:6.6px;text-align:justify}
.note b{font-family:"Barlow Semi Condensed",Arial,sans-serif;font-weight:600;font-size:7px;color:var(--navy-ink);letter-spacing:.2px}
.posture-photo{position:absolute;border-radius:2px}
.ph-lying{background:linear-gradient(180deg,#e8c9a8 0%,#8d2f35 22%,#1f8fc4 45%,#5a4aa0 70%,#1f8fc4 100%)}
.ph-child{background:linear-gradient(200deg,#8d2f35 0%,#b94e3a 40%,#d9852f 70%,#1f8fc4 100%)}
.ph-wall{background:linear-gradient(180deg,#5a4aa0 0%,#6a5bb0 45%,#8d2f35 75%,#1f8fc4 100%)}

/* about */
.about-title{left:59px;top:30px;font-family:"Barlow Semi Condensed",Arial,sans-serif;font-weight:700;font-size:14px;color:var(--on-navy);letter-spacing:.2px}
.about-text{left:59px;top:58px;width:256px;font-size:5.6px;line-height:7.4px;color:var(--on-navy);text-align:justify}
.quote{position:absolute;left:59px;width:260px;color:var(--on-navy);font-size:5.6px;line-height:7.4px}
.quote-mark{position:absolute;left:0;top:-2px;font-family:Georgia,serif;font-size:30px;line-height:24px;color:transparent;-webkit-text-stroke:.8px var(--copper)}
.quote-text{margin-left:34px}
.about-art{left:0;top:0}
.website{left:215px;top:394px;font-size:10px;color:var(--on-navy)}
</style>
</head>
<body>

<section class="page page--cover">
  <div class="abs cover-photo" role="img" aria-label="Teacher seated cross-legged meditating outdoors on grass"></div>
  <div class="abs cover-band"></div>
  <svg class="abs cover-curve" width="365" height="517" viewBox="0 0 365 517" aria-hidden="true">
    <path d="M0 0 L110 0 C64 130 59 390 116 517 L0 517 Z" fill="var(--copper)"/>
    <path d="M0 0 L101 0 C55 130 50 390 107 517 L0 517 Z" fill="var(--navy)"/>
  </svg>
  <div class="abs brand">
    <div class="brand-dot"></div>
    <div class="brand-name">Luna Vesper</div>
    <div class="brand-tagline">Be the change you wish to see in the world</div>
  </div>
  <h1 class="abs cover-title">Yoga for Sleep Workshop and<br>Restorative Yoga Practice</h1>
</section>

<section class="page page--sequence-a">
  <h2 class="abs sequence-title">Yoga for Sleep Workshop Restorative Yoga Sleep Sequence</h2>
  <div class="abs sequence-intro">
    <p>Use this sequence to relax and unwind at the end of a day or before bed. Settle comfortably into each posture for about 5-7 minutes. Set a timer to let you know when it is time to change position, and you can also listen to any music you find relaxing at the same time. The audio recording from the Yoga for Sleep Workshop can also be used to recreate the practice at home.</p>
    <p>In the middle of the night when you can't sleep, you might like to try getting up and resting in any one of these postures for about 5-10 minutes before heading back to bed.</p>
  </div>

  <article class="card" style="top:110px;height:177px">
    <span class="tag" style="left:13px;top:12px">POSTURE 1 –</span>
    <h3 class="posture-name" style="left:13px;top:30px">Supported Chest Opening with<br>Knee Support</h3>
    <p class="note" style="left:13px;top:58px;width:122px"><b>PROPS –</b> 2 x bolsters (or towels rolled up lengthways), 1 x cushion for head support (optional)</p>
    <p class="note" style="left:13px;top:84px;width:122px"><b>SET UP NOTES –</b> Position the props in a T-position with one bolster/towel running parallel to the yoga mat and one bolster towel running horizontal to the mat underneath the knees. Position yourself so your buttocks is on the floor and the parallel bolster runs from the lower back up to behind the head.</p>
    <p class="note" style="left:13px;top:144px;width:293px"><b>CAUTION –</b> If any lower back pain is experience adjust the parallel bolster height by using a towel. If using a towel, the height of the parallel support prop can be adjusted by either using a thinner towel or loosely rolling the towel. Do not us any parallel support prop if pain continues.</p>
    <div class="posture-photo ph-lying" style="left:144px;top:10px;width:88px;height:132px" role="img" aria-label="Lying back on a lengthways bolster with a bolster under the knees"></div>
    <div class="posture-photo ph-lying" style="left:253px;top:10px;width:47px;height:130px" role="img" aria-label="Sitting up in front of the T-shaped bolster setup"></div>
  </article>

  <article class="card" style="top:308px;height:189px">
    <div class="posture-photo ph-lying" style="left:2px;top:36px;width:96px;height:115px" role="img" aria-label="Bound-angle pose with knees supported by pillows"></div>
    <div class="posture-photo ph-lying" style="left:101px;top:28px;width:74px;height:125px" role="img" aria-label="Bound-angle pose with knees supported by yoga blocks"></div>
    <span class="tag" style="left:182px;top:9px">POSTURE 2 –</span>
    <h3 class="posture-name" style="left:182px;top:28px">Supported Bound-Angle Pose</h3>
    <p class="note" style="left:182px;top:45px;width:122px"><b>PROPS –</b> 1 x bolsters (or towel rolled up lengthways), 2 x yoga blocks/bolsters (or pillows), 1 x cushion for head support (optional)</p>
    <p class="note" style="left:182px;top:80px;width:122px"><b>SET UP NOTES –</b><br>Similar to Posture 1 without the bolster behind the knees. Instead, the soles of the feet are together with knees wide being supported by either blocks, bolsters or pillows.</p>
    <p class="note" style="left:182px;top:128px;width:122px"><b>CAUTION –</b><br>If any lower back pain is experience adjust the parallel bolster height by using a towel. If using a towel, the height of the parallel support prop can be adjusted by either using a thinner towel or loosely rolling the towel. Do not us any parallel support prop if pain continues.</p>
  </article>
</section>

<section class="page page--sequence-b">
  <article class="card" style="top:18px;height:179px">
    <span class="tag" style="left:13px;top:6px">POSTURE 3 –</span>
    <h3 class="posture-name" style="left:13px;top:25px">Elevated Legs-Up-the-Wall Pose</h3>
    <p class="note" style="left:13px;top:39px;width:122px"><b>PROPS –</b> 1 x bolsters (or towel or blanket densely folded to a width of about 15-30cm), 1 x cushion for head support (optional)</p>
    <p class="note" style="left:13px;top:75px;width:122px"><b>SET UP NOTES –</b> To enter the posture sit at 90 degrees to the wall with the side of your hip about a hand width away from the wall, and the bolster/folded towel or blanket close by. Lie down on the mat on your side then roll onto your back and extend feet up wall. The feet can push into the wall to elevate the hips slightly so the bolster/folded towel or blanket can slide underneath the hips. The prop should be positioned underneath the sacrum (flat bony structure at the base of the spine).</p>
    <p class="note" style="left:13px;top:155px;width:293px"><b>CAUTION –</b> If any lower back pain is experience adjust the height the hips are elevated by using a towel or blanket that is folded to a lower height.</p>
    <div class="posture-photo ph-wall" style="left:147px;top:12px;width:78px;height:133px" role="img" aria-label="Legs raised up the wall with hips on a folded blanket"></div>
    <div class="posture-photo ph-wall" style="left:224px;top:12px;width:94px;height:133px" role="img" aria-label="Legs raised up the wall with hips on a bolster"></div>
  </article>

  <article class="card" style="top:211px;height:138px">
    <div class="posture-photo ph-child" style="left:11px;top:17px;width:54px;height:92px" role="img" aria-label="Child's pose resting over a bolster, viewed from above"></div>
    <div class="posture-photo ph-child" style="left:76px;top:18px;width:100px;height:92px" role="img" aria-label="Child's pose resting over stacked bed pillows"></div>
    <span class="tag" style="left:188px;top:6px">POSTURE 4 –</span>
    <h3 class="posture-name" style="left:188px;top:25px">Supported Child's Pose</h3>
    <p class="note" style="left:188px;top:40px;width:118px"><b>PROPS –</b> 1-2 x bolsters (or 3-4 bed pillows)</p>
    <p class="note" style="left:188px;top:55px;width:118px"><b>SET UP NOTES –</b> Position bolster or stacked pillows under torso. Rest the head in one direction and remember to turn to the head to the other side half way through the time you spend in this posture.</p>
    <p class="note" style="left:188px;top:99px;width:118px"><b>CAUTION –</b> If any knee or hip pain is experience, increase the height of the support under the torso by adding more bolsters, folded blankets or pillows.</p>
  </article>

  <article class="card" style="top:362px;height:134px">
    <span class="tag" style="left:13px;top:7px">POSTURE 5 –</span>
    <h3 class="posture-name" style="left:13px;top:26px">Basic Relaxation Posture with<br>Knee Support</h3>
    <p class="note" style="left:13px;top:55px;width:122px"><b>PROPS –</b> 1x bolsters (or 1 x bed pillows or rolled up towel)</p>
    <p class="note" style="left:13px;top:81px;width:122px"><b>SET UP NOTES –</b> Reclining on back, position bolster or pillows under knees.</p>
    <div class="posture-photo ph-lying" style="left:155px;top:7px;width:75px;height:120px" role="img" aria-label="Relaxation pose lying on back with a bolster under the knees"></div>
    <div class="posture-photo ph-lying" style="left:245px;top:7px;width:70px;height:120px" role="img" aria-label="Relaxation pose lying on back with pillows under the knees"></div>
  </article>
</section>

<section class="page page--about">
  <svg class="abs about-art" width="365" height="517" viewBox="0 0 365 517">
    <defs>
      <linearGradient id="teacherPhoto" x1="0" y1="0" x2="0" y2="1">
        <stop offset="0" stop-color="#c7a58a"/>
        <stop offset=".3" stop-color="#8d2f35"/>
        <stop offset=".6" stop-color="#5a4aa0"/>
        <stop offset=".85" stop-color="#c9662c"/>
        <stop offset="1" stop-color="#7a4a2a"/>
      </linearGradient>
    </defs>
    <path d="M87 316 C30 370 0 420 -20 517 L253 517 C200 420 140 360 87 316 Z" fill="var(--copper)"/>
    <path d="M87 330 C36 380 8 425 -10 517 L240 517 C192 425 136 372 87 330 Z" fill="url(#teacherPhoto)" role="img" aria-label="Teacher resting in relaxation pose on a yoga mat with a bolster under the knees"/>
  </svg>
  <h2 class="abs about-title">ABOUT THE TEACHER...</h2>
  <p class="abs about-text">Mira Holloway is a current serving Navy Officer, Yoga Therapist (C-YTA) and DeepRest Level 2 instructor. Miranda's classes are about using the practices and teaching of Yoga to come to the essence of your true self and learning to tap into the internal wisdom which is always present. Mira is dedicated to making the resilience developing practices of Yoga accessible to all Australian Military personnel and their families.</p>
  <div class="quote" style="top:112px"><span class="quote-mark">“</span><p class="quote-text">“Posture should be steady and comfortable”<br><br>—Ancient Yoga Sutras</p></div>
  <div class="quote" style="top:153px"><span class="quote-mark">“</span><p class="quote-text">“Tension is who you think you are, Relaxation is who you actually are”</p></div>
  <div class="quote" style="top:186px"><span class="quote-mark">“</span><p class="quote-text">“Life isn't as serious as the mind makes it out to be”<br>—Elias Thorne</p></div>
  <div class="quote" style="top:226px"><span class="quote-mark">“</span><p class="quote-text">“Watch your thoughts, they become words<br>Watch your words, they become actions<br>Watch your actions, they become habits<br>Watch your habits, they become character<br>Watch your character, for it becomes your destiny”<br>—Upanishads</p></div>
  <p class="abs website">www.lunavesperflow.com.au</p>
</section>

</body>
</html>
```